Layout für Broschüre für chemiefreie Lösung, Kühlwasser aufzubereiten
Zielgruppe
VELTROMAX hat eine Technologie entwickelt, die in der Industrie eingesetzt wird um in geschlossenen und offenen Kühlkreisläufen ohne Biozide und Korrosion Inhibitoren das Kühlwasser aufzubereiten. Mit VELTROMAX haben die Unternehmen eine chemiefreie Lösungen gegen Biofouling, Korrosion und Kalk. Zielgruppe sind alle Unternehmen die etwas produzieren oder Klimaanlagen / Heizungssysteme betreiben. Es geht um zukunftsorientierte und vor allem nachhaltige Technologie ohne Einsatz von Chemie.
Aufgabenstellung
Wir suchen für die Broschüre ein neues Layout, dass geradlinig und klar strukturiert ist, vor allem modern. Die Broschüre sollte DIN A 4 - Format sein in der gewohnten Struktur Umschlagseite innen und außen und 8 - 10 Innenseiten. Im Layout sollte ein roter Faden zu erkennen sein, aber nicht jede Seite gleich aussehen. Die Anlagen sind nur beispielhaft vom bestehenden Material und sollten vom Layout keinesfalls eine Orientierung geben, denn das soll verändert werden. Die Anlagen sind für einen inhaltlichen Überblick.

```html
<!DOCTYPE html>
<html lang="de">
<head>
<meta charset="utf-8">
<title>Broschüre – Innenseiten</title>
<link rel="stylesheet" href="https://fonts.googleapis.com/css2?family=Lato:wght@300;400;700&family=Roboto:wght@400&family=Arimo:wght@700&display=swap">
<style>
  :root {
    --bg: #dcdcda;
    --photo-dark: #2b2320;
    --photo-mid: #4a3f39;
    --photo-light: #8a8178;
    --green: #4cb833;
    --frame-green: #5ccc44;
    --band-grey: #cfcfcd;
    --paper: #f7f7f4;
    --ink: #2a2a2a;
    --ink-soft: #4a4a4a;
    --headline: #e8e6e2;
  }
  * { margin: 0; padding: 0; box-sizing: border-box; }
  html, body { width: 1200px; height: 900px; overflow: hidden; }
  body { background: var(--bg); position: relative; font-family: "Lato", sans-serif; }

  .spread { position: absolute; left: 130px; top: 81px; width: 940px; height: 738px; display: flex; }
  .page { position: relative; width: 470px; height: 738px; overflow: hidden; }

  /* Left page */
  .page--left { background: var(--photo-dark); }
  .page__photo {
    position: absolute; inset: 0;
    background:
      radial-gradient(ellipse at 75% 15%, rgba(160,150,140,.55), transparent 55%),
      radial-gradient(ellipse at 30% 80%, rgba(110,100,92,.35), transparent 60%),
      linear-gradient(180deg, var(--photo-mid) 0%, var(--photo-dark) 55%, #3a302b 100%);
  }
  .quote-frame {
    position: absolute; left: 86px; top: 213px; width: 299px; height: 326px;
    border: 3px solid var(--frame-green);
  }
  .quote-frame__text {
    position: absolute; right: 14px; top: 34px;
    font-family: "Roboto", sans-serif; font-weight: 400;
    font-size: 19px; line-height: 26px; letter-spacing: 1.6px;
    text-transform: uppercase; text-align: right; color: var(--headline);
  }

  /* Right page */
  .page--right { background: var(--paper); }
  .info-band { position: absolute; left: 0; top: 0; width: 470px; height: 264px; background: var(--band-grey); }
  .info-band__text {
    position: absolute; left: 34px; top: 62px; width: 262px;
    font-family: "Arimo", sans-serif; font-weight: 700;
    font-size: 8.6px; line-height: 12.4px; color: var(--ink);
  }
  .info-band__label { color: var(--green); font-size: 11px; }
  .info-band__rule { position: absolute; left: 34px; top: 128px; width: 272px; height: 4px; background: var(--green); }

  .steps { position: absolute; left: 34px; top: 285px; display: flex; gap: 8px; }
  .step { width: 130px; }
  .step__number { font-weight: 300; font-size: 32px; line-height: 40px; color: var(--ink); margin-bottom: 26px; }
  .step__title { font-weight: 400; font-size: 12.5px; color: var(--green); margin-bottom: 10px; }
  .step__text { font-size: 6.3px; line-height: 10.2px; color: var(--ink-soft); margin-bottom: 10px; width: 124px; }

  .page-footer { position: absolute; left: 0; right: 36px; top: 711px; border-top: 1px solid #b9b9b6; }
  .page-footer__label { position: absolute; right: 0; top: 4px; font-size: 7px; color: var(--ink-soft); }
</style>
</head>
<body>
  <main class="spread">
    <section class="page page--left">
      <div class="page__photo" role="img" aria-label="Industrieanlage mit Rohrleitungen und Ventilen, dunkel getönt"></div>
      <div class="quote-frame">
        <p class="quote-frame__text">Lorem ipsum elitr,<br>sed diam nonumy<br>eirmod tempor<br>invidunt ut labore<br>et dolore magna<br>aliquyam erat, sed<br>diam voluptua. at</p>
      </div>
    </section>

    <section class="page page--right">
      <div class="info-band">
        <p class="info-band__text"><span class="info-band__label">Infotext</span> Miliquibus perem acita sum, cus.occaeped maximusa conemporunt quas est, con pro te.Nossimuscient laniatisim in nestius comnim fugia quate dolor simos delectis.Beatis is porrum et ut es atur? Ovit rate et, sum et inisquu ntionet</p>
        <div class="info-band__rule"></div>
      </div>

      <div class="steps">
        <article class="step">
          <p class="step__number">01</p>
          <h2 class="step__title">Titel 1</h2>
          <p class="step__text">Agnis erum hil evenitiant.</p>
          <p class="step__text">Maiorem quia dia volesti onsedi volupta non et hitatque idella suntia voluptam ius nonecabor doloritam nos aut quunto cus dolupta testio tectas autenest nobis seque rerum iunt rem nonsedignat.</p>
          <p class="step__text">Dolor simod es non coree por a verum comnis sernatia verovid quae quaecea tum facerspe liquis sitium sincil tempe reria deliam volupta tempore reria deliam, volecti susam dem sit ipic totatqui sint quoditatur? Daesequam sandi odis magnatatus pero volorum voluptae et aliqui sum dellorecid modipide et ommolorion coreedi seque volupta turibuscidem hit omniatum il is maio quat.</p>
        </article>
        <article class="step">
          <p class="step__number">02</p>
          <h2 class="step__title">Titel 2</h2>
          <p class="step__text">Agnis erum hil evenitiant.</p>
          <p class="step__text">Maiorem quia dia volesti onsedi volupta non et hitatque idella suntia voluptam ius nonecabor doloritam nos aut quunto cus dolupta testio tectas autenest nobis seque rerum iunt rem nonsedignat.</p>
          <p class="step__text">Dolor simod es non coree por a verum comnis sernatia verovid quae quaecea tum facerspe liquis sitium sincil tempe reria deliam, volecti susam dem sit ipic totatqui sint quoditatur? Daesequam sandi odis magnatatus pero volorum voluptae et aliqui sum dellorecid modipide et ommolorion coreedi seque volupta turibuscidem hit omniatum il is.</p>
        </article>
        <article class="step">
          <p class="step__number">03</p>
          <h2 class="step__title">Titel 3</h2>
          <p class="step__text">tempe reria deliam, volecti susam dem sit ipic totatqui sint quoditatur? Daesequam sandi odis magnatatus pero volorum voluptae et aliqui sum dellorecid modipide et ommolorion coreedi seque volupta turibuscidem hit omniatum il is maio quat.</p>
        </article>
      </div>

      <footer class="page-footer"><span class="page-footer__label">Chemiefreie 7</span></footer>
    </section>
  </main>
</body>
</html>
```